Generic Business Card

I need a business card for my new cafe which is only six weeks old. I'm continuously asked for a business so that customers can either keep or pass on to a friend. I'd also like a card that I can give out with each bill which contains the business name, address, contact details and website.
The cafe's internal design has an industrial feel to it with modern subdued colours. I have attached an internal photo along with my main hero shot and logo.
The hero shot features prominently on my website and other print material and I would also like it to appear on my bus card.

Target Market(s)

Men & women between 35 and 45 years of age who know and enjoy good coffee.

Industry/Entity Type

Industrial

Contact Information for Business Card

Shop 7b/118-120 Pelbourne Street, East Dalvington 3981
Tel. 9462 3157
www.talvemo.com.au

```html
<!DOCTYPE html>
<html lang="en">
<head>
<meta charset="utf-8">
<title>Talvemo Business Card</title>
<link rel="stylesheet" href="https://fonts.googleapis.com/css2?family=Questrial&display=swap">
<style>
  :root {
    --card-white: #ffffff;
    --ink: #231f20;
    --band: #1f1d1e;
    --rule-soft: #bdbdbd;
    --photo-dark: #2a2a2a;
    --photo-mid: #8a8a8a;
    --photo-light: #d9d9d9;
    --page: #e9e6e2;
  }
  html, body {
    margin: 0;
    padding: 0;
    width: 1200px;
    height: 750px;
    overflow: hidden;
    background: var(--page);
  }
  .business-card {
    position: relative;
    width: 1200px;
    height: 750px;
    background: var(--card-white);
    font-family: "Questrial", "Century Gothic", sans-serif;
    color: var(--ink);
    overflow: hidden;
  }
  .hero-shot {
    position: absolute;
    left: 0;
    top: 0;
    width: 470px;
    height: 750px;
    background:
      radial-gradient(ellipse at 60% 40%, var(--photo-light) 0%, var(--photo-mid) 35%, transparent 70%),
      linear-gradient(160deg, var(--photo-dark) 0%, var(--photo-mid) 45%, var(--photo-dark) 100%);
  }
  .brand {
    position: absolute;
    left: 520px;
    top: 150px;
    width: 560px;
    text-align: center;
  }
  .brand-name {
    margin: 0;
    font-size: 118px;
    font-weight: 400;
    letter-spacing: 6px;
    line-height: 1;
    color: var(--ink);
  }
  .brand-rule {
    position: absolute;
    left: 530px;
    width: 460px;
    height: 3px;
    background: var(--ink);
    top: 318px;
  }
  .brand-rule--soft {
    top: 356px;
    left: 560px;
    width: 430px;
    height: 2px;
    background: var(--rule-soft);
  }
  .contact-band {
    position: absolute;
    left: 484px;
    top: 440px;
    width: 716px;
    height: 310px;
    background: var(--band);
    box-sizing: border-box;
    padding: 44px 60px 0 0;
    text-align: right;
    color: var(--card-white);
    font-size: 31px;
    line-height: 1.32;
  }
  .contact-band p { margin: 0; }
</style>
</head>
<body>
  <main class="business-card">
    <div class="hero-shot" role="img" aria-label="Black and white photo of a barista pulling an espresso shot from a cafe coffee machine into a cup"></div>

    <div class="brand">
      <h1 class="brand-name">TALVEMO</h1>
    </div>
    <div class="brand-rule"></div>
    <div class="brand-rule brand-rule--soft"></div>

    <section class="contact-band">
      <p class="contact-address">Shop 7b/118-120 Pelbourne Street,<br>East Dalvington 3981</p>
      <p class="contact-phone">Tel. 9462 3157</p>
      <p class="contact-web">www.talvemo.com.au</p>
    </section>
  </main>
</body>
</html>
```